new business card, with new logo. Looking for full design

I would like to have a graphic designer/artist create a high standard, premium business logo and business card design that I can either use to print on my own or have printed through them as well. Also, would be nice if I could customize with new employee names and info afterwards. Also, though I don't have a logo, something that matches the theme here https://larkfieldstrategyadvisors.com/ as well as incorporates the letter "M" is what I am currently thinking. Thanks!

Target Market(s)

High end corporate executives

Industry/Entity Type

Economics

Contact Information for Business Card

Dr. Oscar Teodoro-Lindqvist
Principal Advisor
OTL@LarkfieldStrategyAdvisors.com
other contact/website details from here: https://larkfieldstrategyadvisors.com/

Logo Text

Larkfield Strategy Advisors

```html
<!DOCTYPE html>
<html lang="en">
<head>
<meta charset="utf-8">
<title>Larkfield Strategy Advisors — Business Card</title>
<link href="https://fonts.googleapis.com/css2?family=Crimson+Text:wght@400;600&display=swap" rel="stylesheet">
<style>
  :root {
    --stage: #0c1a21;
    --card-back: #e7e4e7;
    --card-front: #ffffff;
    --rose: #c4857b;
    --ink: #2b2b2e;
  }
  * { margin: 0; padding: 0; box-sizing: border-box; }
  html, body {
    width: 1200px; height: 797px; overflow: hidden;
    background: var(--stage);
    font-family: "Crimson Text", Georgia, serif;
  }
  .stage {
    width: 1200px; height: 797px;
    display: flex; align-items: center; justify-content: center; gap: 40px;
  }
  .card {
    position: relative;
    width: 540px; height: 309px;
    box-shadow: 0 10px 30px rgba(0,0,0,.45);
    overflow: hidden;
  }
  .company-name {
    color: var(--rose);
    font-weight: 400;
    letter-spacing: 0;
    line-height: 1.15;
  }

  /* Back side */
  .card--back { background: var(--card-back); }
  .card--back .company-name {
    position: absolute; left: 0; right: 0; top: 112px;
    text-align: center; font-size: 30px;
  }
  .rule-row {
    position: absolute; left: 0; right: 0; top: 222px;
    display: flex; align-items: center; gap: 14px;
  }
  .rule-row .rule { flex: 1; height: 2px; background: var(--rose); }
  .rule-row .site { color: var(--ink); font-size: 14px; }

  /* Front side */
  .card--front { background: var(--card-front); }
  .card--front .company-name {
    position: absolute; left: 30px; top: 126px; width: 212px;
    text-align: center; font-size: 24px;
  }
  .divider {
    position: absolute; left: 262px; top: 74px; height: 160px; width: 1px;
    background: var(--rose);
  }
  .contact {
    position: absolute; left: 282px; top: 76px; right: 16px;
  }
  .contact__name { color: var(--rose); font-size: 20px; line-height: 1.1; }
  .contact__role { color: var(--ink); font-size: 17px; margin-top: 2px; }
  .contact__line {
    display: flex; align-items: flex-start; gap: 7px;
    color: var(--ink); font-size: 13px; line-height: 1.25; margin-top: 14px;
  }
  .contact__line svg { flex: none; margin-top: 2px; }
</style>
</head>
<body>
<main class="stage">
  <section class="card card--back" aria-label="Card back">
    <div class="company-name">Larkfield Strategy Advisors</div>
    <div class="rule-row">
      <span class="rule"></span>
      <span class="site">larkfieldstrategyadvisors.com</span>
      <span class="rule"></span>
    </div>
  </section>

  <section class="card card--front" aria-label="Card front">
    <div class="company-name">Larkfield Strategy Advisors</div>
    <div class="divider"></div>
    <div class="contact">
      <div class="contact__name">Dr. Oscar Teodoro-Lindqvist</div>
      <div class="contact__role">Principal Advisor</div>
      <div class="contact__line">
        <svg width="11" height="14" viewBox="0 0 11 14" aria-hidden="true">
          <path d="M5.5 1a4 4 0 0 1 4 4c0 3-4 8-4 8s-4-5-4-8a4 4 0 0 1 4-4z" fill="none" stroke="var(--rose)" stroke-width="1.2"/>
          <circle cx="5.5" cy="5" r="1.4" fill="var(--rose)"/>
        </svg>
        <span>2417 Harlow Ave NW, Suite 410<br>Washington, DC 20008</span>
      </div>
      <div class="contact__line">
        <svg width="13" height="13" viewBox="0 0 13 13" aria-hidden="true">
          <circle cx="6.5" cy="6.5" r="5.6" fill="none" stroke="var(--rose)" stroke-width="1.2"/>
          <circle cx="6.5" cy="6.5" r="2.2" fill="none" stroke="var(--rose)" stroke-width="1.2"/>
        </svg>
        <span>OTL@LarkfieldStrategyAdvisors.com</span>
      </div>
    </div>
  </section>
</main>
</body>
</html>
```